Australian IT Company requires Business Card Design

Bluepeak is an Australian company that specialises in IT consulting & support, software development, project management, network services.

We have been in business for 15 years.

* We require a business card with the following on it:
Logo
Address
Contact Details
Space for staff name, title & mobile number

Industry/Entity Type

Software

```html
<!DOCTYPE html>
<html lang="en">
<head>
<meta charset="utf-8">
<title>Bluepeak Business Card</title>
<link rel="stylesheet" href="https://fonts.googleapis.com/css2?family=Courier+Prime:wght@400;700&display=swap">
<style>
  :root {
    --backdrop: #3ba8bb;
    --card: #ffffff;
    --brand-blue: #1466a0;
    --text-blue: #1f5f8f;
    --rule-grey: #6b6b6d;
    --band-grey: #666668;
    --faint: #f1f2f7;
    --icon-bg: #dfe6ee;
  }
  * { margin: 0; padding: 0; box-sizing: border-box; }
  html, body { width: 1200px; height: 814px; overflow: hidden; }
  body {
    background: var(--backdrop);
    font-family: "Courier Prime", "Courier New", monospace;
    position: relative;
  }
  .card {
    position: absolute;
    left: 100px; top: 97px;
    width: 1000px; height: 620px;
    background: var(--card);
    overflow: hidden;
    box-shadow: 0 8px 24px rgba(0,0,0,0.18);
  }
  .rule-vertical {
    position: absolute; left: 462px; top: 0;
    width: 8px; height: 136px; background: var(--rule-grey);
  }
  .rule-horizontal {
    position: absolute; left: 462px; top: 130px;
    width: 456px; height: 7px; background: var(--rule-grey);
  }
  .brand {
    position: absolute; left: 484px; top: 62px;
    display: flex; align-items: center; gap: 22px;
  }
  .brand-mark {
    width: 52px; height: 52px; background: var(--brand-blue);
  }
  .brand-name {
    font-weight: 700; font-size: 48px; color: var(--brand-blue);
    letter-spacing: 1px; line-height: 1;
  }
  .backdrop-square {
    position: absolute; left: 573px; top: 190px;
    width: 323px; height: 320px; background: var(--faint);
  }
  .address {
    position: absolute; left: 117px; top: 190px;
    font-weight: 700; font-size: 33px; line-height: 41px;
    color: var(--text-blue);
  }
  .contacts {
    position: absolute; left: 117px; top: 360px;
    list-style: none;
  }
  .contacts li {
    display: flex; align-items: center; gap: 14px;
    height: 54px; font-size: 24px; color: var(--text-blue);
  }
  .contact-icon {
    width: 28px; height: 28px; background: var(--icon-bg);
    display: flex; align-items: center; justify-content: center;
  }
  .band-blue {
    position: absolute; left: 58px; top: 540px;
    width: 884px; height: 80px; background: var(--brand-blue);
  }
  .band-grey {
    position: absolute; left: 58px; top: 558px;
    width: 672px; height: 62px; background: var(--band-grey);
    border-top: 5px solid var(--card); border-right: 5px solid var(--card);
  }
</style>
</head>
<body>
  <article class="card">
    <div class="rule-vertical"></div>
    <div class="rule-horizontal"></div>
    <div class="brand">
      <span class="brand-mark"></span>
      <span class="brand-name">BLUEPEAK</span>
    </div>
    <div class="backdrop-square"></div>
    <address class="address">
      14 Ridgeway Lane<br>
      Summit House 3<br>
      Carlton Vic 3053
    </address>
    <ul class="contacts">
      <li>
        <span class="contact-icon">
          <svg width="18" height="18" viewBox="0 0 18 18" aria-hidden="true">
            <path d="M4 2h3l1 4-2 1.5a9 9 0 0 0 4.5 4.5L12 10l4 1v3a2 2 0 0 1-2 2A12 12 0 0 1 2 4a2 2 0 0 1 2-2z" fill="#1f5f8f"/>
          </svg>
        </span>
        +61 3 9555 0182
      </li>
      <li>
        <span class="contact-icon">
          <svg width="18" height="18" viewBox="0 0 18 18" aria-hidden="true">
            <rect x="2" y="4" width="14" height="10" fill="none" stroke="#1f5f8f" stroke-width="1.6"/>
            <path d="M2 4l7 6 7-6" fill="none" stroke="#1f5f8f" stroke-width="1.6"/>
          </svg>
        </span>
        (staff members email address)
      </li>
      <li>
        <span class="contact-icon">
          <svg width="18" height="18" viewBox="0 0 18 18" aria-hidden="true">
            <circle cx="9" cy="9" r="7" fill="none" stroke="#1f5f8f" stroke-width="1.5"/>
            <ellipse cx="9" cy="9" rx="3" ry="7" fill="none" stroke="#1f5f8f" stroke-width="1.2"/>
            <path d="M2 9h14" stroke="#1f5f8f" stroke-width="1.2"/>
          </svg>
        </span>
        www.bluepeak.net.au
      </li>
    </ul>
    <div class="band-blue"></div>
    <div class="band-grey"></div>
  </article>
</body>
</html>
```